A start-up named "trovamind" - a clinical research organization needs a new PowerPoint design

We need a new PowerPoint Design (incl. business card and stationery design) for an early-stage start-up named "trovamind" seeking to build an ecosystem/ strategic partner alliances or consortium of committed and active collaborators to guide important components of the clinical trial.

Our ultimate goal is to avoid false neutrals – therapies that have not been and may never be evaluated in clinical trials due to the costs and/ or complexity.

The final design should highlight our patient-centric approach, innovative study design supported with the novel AI platform to make a stronger impact on patient lives.

Please see the attached brief for more details.
Updates

Requesting the proposals on color-coding, business-card designs, clinical research visuals, and icons as well as stationery design.

Target Market(s)

Pharma/ Biotech Executives
Medical Institutions
Clinical Trial Participants (Patients)

Colors
e34398

Requirements
Must have
• Use the Color Version of purple/ magenta logo

```html
<!DOCTYPE html>
<html lang="en">
<head>
<meta charset="utf-8">
<title>Target Audience: Decision Makers</title>
<link rel="stylesheet" href="https://fonts.googleapis.com/css2?family=Open+Sans:wght@400;600;700&display=swap">
<style>
  :root {
    --magenta: #e34398;
    --green: #92d050;
    --blue: #0a88d4;
    --amber: #ffc000;
    --ink: #262626;
    --card-bg: #f2f2f2;
    --badge-bg: #ececec;
    --page-bg: #e0e0e0;
    --white: #ffffff;
  }
  * { margin: 0; padding: 0; box-sizing: border-box; }
  html, body { width: 1200px; height: 675px; overflow: hidden; background: var(--white); }
  body { font-family: "Open Sans", Arial, sans-serif; color: var(--ink); }
  .slide { position: relative; width: 1200px; height: 675px; overflow: hidden; }

  .slide-title {
    position: absolute; left: 56px; top: 66px;
    font-size: 41px; font-weight: 700; color: var(--magenta); line-height: 1.15;
  }
  .slide-subtitle {
    position: absolute; left: 56px; top: 113px;
    font-size: 28px; font-weight: 400; color: var(--ink); line-height: 1.2;
  }

  .role-card {
    position: absolute; top: 261px; width: 250px; height: 288px;
    background: var(--card-bg); border-radius: 8px;
    box-shadow: 0 2px 6px rgba(0,0,0,0.12);
  }
  .role-card.economic { left: 56px; --accent: var(--magenta); }
  .role-card.influencers { left: 336px; --accent: var(--green); }
  .role-card.champion { left: 616px; --accent: var(--blue); }
  .role-card.veto { left: 896px; --accent: var(--amber); }

  .role-header {
    height: 98px; background: var(--accent); border-radius: 8px 8px 0 0;
    display: flex; align-items: flex-end; justify-content: center; padding-bottom: 18px;
    color: var(--white); font-size: 21px; font-weight: 700;
  }
  .role-icon {
    position: absolute; left: 78px; top: -57px; width: 94px; height: 94px;
    border-radius: 50%; background: var(--badge-bg);
    display: flex; align-items: center; justify-content: center;
  }
  .role-icon svg { width: 50px; height: 50px; stroke: var(--accent); fill: none; stroke-width: 1.6; stroke-linecap: round; stroke-linejoin: round; }

  .role-list { list-style: none; padding: 22px 16px 0 20px; }
  .role-list li {
    position: relative; padding-left: 30px; font-size: 19px; line-height: 24px; color: var(--ink);
  }
  .role-list li::before {
    content: "•"; position: absolute; left: 6px; top: 0; font-size: 17px;
  }

  .brand-name {
    position: absolute; left: 56px; top: 604px;
    font-size: 30px; font-weight: 600; color: var(--ink); line-height: 1.2;
  }

  .page-number {
    position: absolute; left: 1101px; top: 601px; width: 42px; height: 42px;
    border-radius: 50%; background: var(--page-bg);
    display: flex; align-items: center; justify-content: center;
    font-size: 15px; font-weight: 600; color: var(--ink);
  }
</style>
</head>
<body>
<main class="slide">
  <h1 class="slide-title">Target Audience: Decision Makers</h1>
  <p class="slide-subtitle">Based at the pharma companies; highly complex (one DMU for each drug);</p>

  <section class="role-card economic">
    <div class="role-icon">
      <svg viewBox="0 0 50 50" aria-hidden="true">
        <path d="M8 6 V42 H46"/>
        <path d="M8 42 l4 -3 M8 42 l4 3"/>
        <path d="M12 10 C22 36 32 40 44 40"/>
        <path d="M12 38 C24 34 34 20 42 8"/>
        <path d="M42 8 l-4 1 M42 8 l0 4"/>
      </svg>
    </div>
    <h2 class="role-header">Economic buyer</h2>
    <ul class="role-list">
      <li>Global Program Leader</li>
    </ul>
  </section>

  <section class="role-card influencers">
    <div class="role-icon">
      <svg viewBox="0 0 50 50" aria-hidden="true">
        <circle cx="12" cy="18" r="4.5"/>
        <circle cx="38" cy="18" r="4.5"/>
        <circle cx="25" cy="26" r="4.5"/>
        <path d="M4 32 c0 -6 4 -8 8 -8 c3 0 5 1 6 3"/>
        <path d="M46 32 c0 -6 -4 -8 -8 -8 c-3 0 -5 1 -6 3"/>
        <path d="M16 40 c0 -6 4 -8 9 -8 s9 2 9 8"/>
      </svg>
    </div>
    <h2 class="role-header">Influencers</h2>
    <ul class="role-list">
      <li>Clinical Operations Leader</li>
      <li>Head Development Operations</li>
    </ul>
  </section>

  <section class="role-card champion">
    <div class="role-icon">
      <svg viewBox="0 0 50 50" aria-hidden="true">
        <path d="M14 6 H36 V18 C36 26 31 30 25 30 C19 30 14 26 14 18 Z"/>
        <path d="M14 10 H7 C7 20 11 22 15 22"/>
        <path d="M36 10 H43 C43 20 39 22 35 22"/>
        <path d="M25 30 V38"/>
        <path d="M18 38 H32 L34 44 H16 Z"/>
      </svg>
    </div>
    <h2 class="role-header">Champion</h2>
    <ul class="role-list">
      <li>Medical Director</li>
      <li>R&amp;D Innovation/Digital Heads</li>
    </ul>
  </section>

  <section class="role-card veto">
    <div class="role-icon">
      <svg viewBox="0 0 50 50" aria-hidden="true">
        <path d="M25 4 V42"/>
        <path d="M8 12 H42"/>
        <path d="M16 44 H34"/>
        <path d="M11 12 L5 28 H17 Z"/>
        <path d="M39 12 L33 26 H45 Z"/>
        <path d="M5 28 c2 4 10 4 12 0"/>
        <path d="M33 26 c2 4 10 4 12 0"/>
      </svg>
    </div>
    <h2 class="role-header">Veto</h2>
    <ul class="role-list">
      <li>Chief Financial Officer</li>
    </ul>
  </section>

  <div class="brand-name">trovamind</div>

  <div class="page-number">9</div>
</main>
</body>
</html>
```